Design of a carbonated cola drink

our competitor is selling brindle cola
their design is en closed
we need a similar design colours but we cant use
brindle cola
we were thinking of usuing
the words KVO cola
using a bit of the american flag colors red and blue
designs for three flavors shown below should be shown
the main drink colour is zapp red
orange bluma orange
punch like wintzel /zolvin burst

Target Market(s)

pacific islands

Requirements
Must have
• mentioned above
Nice to have
• mentioned above

```html
<!DOCTYPE html>
<html lang="en">
<head>
<meta charset="utf-8">
<title>KVO Cola – Flavour Range Labels</title>
<link rel="stylesheet" href="https://fonts.googleapis.com/css2?family=Montserrat:wght@800;900&display=swap">
<style>
  :root {
    --page: #ffffff;
    --metal-light: #eceef0;
    --metal-mid: #c9ccd0;
    --metal-dark: #a9adb2;
    --brand-white: #f6f4f0;

    --cola-band: #1d2a6e;
    --cola-deep: #7a0710;
    --cola-main: #b8121d;
    --cola-word: #ec2a3c;

    --orange-band: #ec6e12;
    --orange-deep: #d3180e;
    --orange-main: #ee8a10;
    --orange-word: #e5230f;

    --punch-band: #45b366;
    --punch-deep: #063d17;
    --punch-main: #137a30;
    --punch-word: #22e05c;
  }
  * { margin: 0; padding: 0; box-sizing: border-box; }
  html, body { width: 1200px; height: 1200px; overflow: hidden; background: var(--page); }
  .range {
    position: relative;
    width: 1200px; height: 1200px;
    display: flex; justify-content: center; align-items: center; gap: 56px;
  }
  .label { width: 332px; height: 888px; display: block; }
  .label-metal { rx: 14; }
  .brand-name {
    font-family: "Montserrat", sans-serif;
    font-weight: 900;
    fill: var(--brand-white);
  }
  .flavour-name {
    font-family: "Montserrat", sans-serif;
    font-weight: 900;
  }
  .label--cola .band { fill: var(--cola-band); }
  .label--cola .flavour-name { fill: var(--cola-word); }
  .label--orange .band { fill: var(--orange-band); }
  .label--orange .flavour-name { fill: var(--orange-word); }
  .label--punch .band { fill: var(--punch-band); }
  .label--punch .flavour-name { fill: var(--punch-word); }
  .band-edge { fill: #ffffff; opacity: 0.55; }
</style>
</head>
<body>
<main class="range">

  <!-- Cola -->
  <svg class="label label--cola" viewBox="0 0 332 888" aria-label="KVO Cola label">
    <defs>
      <linearGradient id="metal-cola" x1="0" x2="1" y1="0" y2="0">
        <stop offset="0" stop-color="var(--metal-dark)"/>
        <stop offset="0.3" stop-color="var(--metal-light)"/>
        <stop offset="0.7" stop-color="var(--metal-mid)"/>
        <stop offset="1" stop-color="var(--metal-dark)"/>
      </linearGradient>
      <linearGradient id="panel-cola" x1="0" x2="1" y1="0" y2="0">
        <stop offset="0" stop-color="var(--cola-deep)"/>
        <stop offset="0.4" stop-color="var(--cola-main)"/>
        <stop offset="1" stop-color="var(--cola-deep)"/>
      </linearGradient>
    </defs>
    <rect class="label-metal" x="0" y="0" width="332" height="888" rx="14" fill="url(#metal-cola)"/>
    <polygon class="panel" points="0,270 332,118 332,642 0,812" fill="url(#panel-cola)"/>
    <polygon class="band" points="0,228 332,76 332,118 0,270"/>
    <polygon class="band-edge" points="0,270 332,118 332,121 0,273"/>
    <polygon class="band" points="0,812 332,642 332,684 0,854"/>
    <polygon class="band-edge" points="0,809 332,639 332,642 0,812"/>
    <text class="brand-name" transform="translate(194,652) rotate(-90)" font-size="152" textLength="410" lengthAdjust="spacingAndGlyphs">KVO</text>
    <text class="flavour-name" transform="translate(270,640) rotate(-90)" font-size="102" textLength="250" lengthAdjust="spacingAndGlyphs">COLA</text>
  </svg>

  <!-- Orange -->
  <svg class="label label--orange" viewBox="0 0 332 888" aria-label="KVO Orange label">
    <defs>
      <linearGradient id="metal-orange" x1="0" x2="1" y1="0" y2="0">
        <stop offset="0" stop-color="var(--metal-dark)"/>
        <stop offset="0.3" stop-color="var(--metal-light)"/>
        <stop offset="0.7" stop-color="var(--metal-mid)"/>
        <stop offset="1" stop-color="var(--metal-dark)"/>
      </linearGradient>
      <linearGradient id="panel-orange" x1="0" x2="1" y1="0" y2="1">
        <stop offset="0" stop-color="var(--orange-deep)"/>
        <stop offset="0.45" stop-color="var(--orange-main)"/>
        <stop offset="1" stop-color="var(--orange-deep)"/>
      </linearGradient>
    </defs>
    <rect class="label-metal" x="0" y="0" width="332" height="888" rx="14" fill="url(#metal-orange)"/>
    <polygon class="panel" points="0,270 332,118 332,642 0,812" fill="url(#panel-orange)"/>
    <polygon class="band" points="0,228 332,76 332,118 0,270"/>
    <polygon class="band-edge" points="0,270 332,118 332,121 0,273"/>
    <polygon class="band" points="0,812 332,642 332,684 0,854"/>
    <polygon class="band-edge" points="0,809 332,639 332,642 0,812"/>
    <text class="brand-name" transform="translate(194,652) rotate(-90)" font-size="152" textLength="410" lengthAdjust="spacingAndGlyphs">KVO</text>
    <text class="flavour-name" transform="translate(264,652) rotate(-90)" font-size="86" textLength="330" lengthAdjust="spacingAndGlyphs">ORANGE</text>
  </svg>

  <!-- Punch -->
  <svg class="label label--punch" viewBox="0 0 332 888" aria-label="KVO Punch label">
    <defs>
      <linearGradient id="metal-punch" x1="0" x2="1" y1="0" y2="0">
        <stop offset="0" stop-color="var(--metal-dark)"/>
        <stop offset="0.3" stop-color="var(--metal-light)"/>
        <stop offset="0.7" stop-color="var(--metal-mid)"/>
        <stop offset="1" stop-color="var(--metal-dark)"/>
      </linearGradient>
      <linearGradient id="panel-punch" x1="0" x2="1" y1="0" y2="0">
        <stop offset="0" stop-color="var(--punch-main)"/>
        <stop offset="0.5" stop-color="var(--punch-main)"/>
        <stop offset="1" stop-color="var(--punch-deep)"/>
      </linearGradient>
    </defs>
    <rect class="label-metal" x="0" y="0" width="332" height="888" rx="14" fill="url(#metal-punch)"/>
    <polygon class="panel" points="0,270 332,118 332,642 0,812" fill="url(#panel-punch)"/>
    <polygon class="band" points="0,228 332,76 332,118 0,270"/>
    <polygon class="band-edge" points="0,270 332,118 332,121 0,273"/>
    <polygon class="band" points="0,812 332,642 332,684 0,854"/>
    <polygon class="band-edge" points="0,809 332,639 332,642 0,812"/>
    <text class="brand-name" transform="translate(194,652) rotate(-90)" font-size="152" textLength="410" lengthAdjust="spacingAndGlyphs">KVO</text>
    <text class="flavour-name" transform="translate(270,652) rotate(-90)" font-size="96" textLength="272" lengthAdjust="spacingAndGlyphs">PUNCH</text>
  </svg>

</main>
</body>
</html>
```